ROBERTO VENTRANZI and his Orchestra "Under The Lanterns"

Music event. Friday November 6, 2015. Doors open 7pm
Venue - The Harwell Lane Hall, 47 Dunmore Rd. Perth. WA. 6000.
Roberto and his 12 piece band will perform inside a boxing ring in a very funky viby venue "The Harwell Lane Hall" in Perth, WA. The venue is a gorgeous retro looking place. See pics attached.
This "live music" event is focused on Roberto Ventranzi - with a twist. The 12 piece band and Roberto will be performing in the boxing ring - a really cool and quirky concept.
The whole event will be filmed and recorded - to make a DVD.
Updates

please don't focus on boxing this is a music event - the 11 piece band will perform in the boxing ring doesn't need to look "tough guy"

Target Market(s)

music lovers - 35 to 70. It needs to feel funky but still elegant focus to a mature fun loving audience "who have seen it all before".
Glitterati and Media event. Food lovers.....Tavolino Event Catering to provide italian tapas food included in the ticket price from 7pm to 8:30pm .....also includes 2 complimentary drinks

Industry/Entity Type

Gym

Font styles to use
Sans Serif

Requirements
Must have
• A powerful focus on Roberto Ventranzi and his band . . . and his music.
• A "wow factor" of it being "Under The Lanterns" a totally new concept in Perth nightlife entertainment. Basically, the boxing ring is the stage. ALSO, please mention that this event will be filmed with 8 cameras and digitally recorded. A 5.1 surround sound DVD will be made of this event . . . and we want "you" (the people) to be a part of it. And we'll have cameramen going through the crowd interviewing everyone for the "behind the scenes" section of the DVD. This is a super-exclusive event. Only 150 tix available - so get in quick.
Nice to have
• Included in the ticket price of $100 is 2 complimentary drinks (beer/wine/bubbly) and lots of delicious italian tapas food from 7pm to 8:30pm - provided by Tavolino Events Catering. Extra drinks including spirits and cocktails can be purchased at the bar. Show starts at 8:30pm sharp.
Should not have
• no typical Italian anything please

```html
<!DOCTYPE html>
<html lang="en">
<head>
<meta charset="utf-8">
<title>Roberto Ventranzi and his Orchestra – Under The Lanterns</title>
<link rel="stylesheet" href="https://fonts.googleapis.com/css2?family=Raleway:wght@200;300;400&family=Oswald:wght@400;600;700&family=Archivo+Narrow:ital,wght@0,500;1,500;1,600&display=swap">
<style>
  :root {
    --ink: #141210;
    --ink-warm: #2a221c;
    --yellow: #f3d21d;
    --white: #f4f1ea;
    --grey: #cfc9bf;
    --amber: #6b4a2a;
  }
  * { margin: 0; padding: 0; box-sizing: border-box; }
  html, body { width: 849px; height: 1200px; overflow: hidden; background: var(--ink); }
  .poster {
    position: relative;
    width: 849px;
    height: 1200px;
    overflow: hidden;
    background: linear-gradient(180deg, #1d1915 0%, #15120f 55%, #181512 100%);
    color: var(--white);
    font-family: "Archivo Narrow", sans-serif;
  }
  .venue-photo {
    position: absolute;
    left: 0; top: 0;
    width: 849px; height: 520px;
    background:
      radial-gradient(ellipse at 20% 30%, rgba(150,100,60,.55) 0%, rgba(80,55,35,.3) 35%, transparent 65%),
      linear-gradient(180deg, #3a2e24 0%, #221b16 60%, transparent 100%);
  }
  .portrait {
    position: absolute;
    left: 370px; top: 0;
    width: 479px; height: 800px;
    background:
      radial-gradient(ellipse at 55% 28%, rgba(150,135,120,.55) 0%, rgba(90,80,70,.35) 30%, transparent 60%),
      linear-gradient(180deg, rgba(70,62,55,.5) 0%, rgba(30,26,22,.2) 70%, transparent 100%);
  }
  .recording-note {
    position: absolute;
    left: 50px; top: 28px;
    font-style: italic; font-weight: 600;
    font-size: 21px; letter-spacing: .5px;
    color: var(--yellow);
  }
  .artist {
    position: absolute;
    left: 50px; top: 100px;
    font-family: "Raleway", sans-serif;
    font-weight: 300;
    font-size: 58px;
    letter-spacing: 1px;
    color: var(--white);
    line-height: 1;
  }
  .ensemble {
    position: absolute;
    left: 52px; top: 168px;
    font-family: "Raleway", sans-serif;
    font-weight: 400;
    font-size: 26px;
    color: var(--white);
  }
  .event-title {
    position: absolute;
    left: 268px; top: 318px;
    font-style: italic; font-weight: 600;
    font-size: 44px;
    color: var(--yellow);
    letter-spacing: .5px;
  }
  .date-day {
    position: absolute;
    left: 270px; top: 372px;
    width: 36px; height: 176px;
    background: var(--yellow);
    color: var(--ink);
    display: flex; align-items: center; justify-content: center;
  }
  .date-day span {
    transform: rotate(-90deg);
    font-family: "Oswald", sans-serif; font-weight: 600;
    font-size: 30px; letter-spacing: 2px; white-space: nowrap;
  }
  .date-month {
    position: absolute;
    left: 318px; top: 376px;
    font-family: "Oswald", sans-serif; font-weight: 600;
    font-size: 40px; line-height: 1;
    color: var(--white);
  }
  .date-number {
    position: absolute;
    left: 312px; top: 400px;
    font-family: "Oswald", sans-serif; font-weight: 700;
    font-size: 160px; line-height: 1;
    color: var(--white);
  }
  .venue {
    position: absolute;
    left: 56px; top: 590px;
  }
  .venue-name {
    font-style: italic; font-weight: 600;
    font-size: 34px; color: var(--yellow);
  }
  .venue-address {
    font-weight: 500; font-size: 30px; color: var(--white); margin-top: 4px;
  }
  .doors {
    position: absolute;
    left: 640px; top: 594px;
    text-align: right;
  }
  .doors-label { font-weight: 500; font-size: 24px; color: var(--white); }
  .doors-time {
    font-family: "Oswald", sans-serif; font-weight: 400;
    font-size: 46px; color: var(--white); line-height: 1.1;
  }
  .divider {
    position: absolute;
    left: 50px; width: 749px; height: 2px;
    background: var(--grey); opacity: .6;
  }
  .exclusive {
    position: absolute;
    left: 0; width: 849px; top: 744px;
    text-align: center;
    font-weight: 500; font-size: 24px; letter-spacing: .5px;
    color: var(--white);
  }
  .caterer-mark {
    position: absolute;
    left: 50px; top: 826px;
    display: flex; align-items: center; gap: 8px;
  }
  .caterer-mark .square {
    width: 22px; height: 22px; background: var(--amber);
  }
  .caterer-mark .name {
    font-weight: 500; font-size: 15px; color: var(--white); line-height: 1.1;
  }
  .package {
    position: absolute;
    left: 172px; top: 800px;
    font-weight: 500; font-size: 22px; line-height: 29px;
    text-align: center; width: 560px;
    color: var(--white);
  }
  .package .highlight { color: var(--yellow); font-style: italic; }
</style>
</head>
<body>
<main class="poster">
  <div class="venue-photo" role="img" aria-label="Warm, softly blurred interior of a retro bar venue"></div>
  <div class="portrait" role="img" aria-label="Photograph of the bandleader in a dark suit, singing"></div>

  <p class="recording-note">LIVE RECORDING 8 CAMERAS AND DIGITALLY RECORDED IN 5.1 SURROUND SOUND</p>
  <h1 class="artist">ROBERTO VENTRANZI</h1>
  <p class="ensemble">AND HIS ORCHESTRA</p>

  <h2 class="event-title">UNDER THE LANTERNS</h2>
  <div class="date-day"><span>FRIDAY</span></div>
  <p class="date-month">NOVEMBER</p>
  <p class="date-number">06</p>

  <div class="venue">
    <p class="venue-name">THE HARWELL LANE HALL</p>
    <p class="venue-address">47 Dunmore Rd. Perth. WA. 6000.</p>
  </div>
  <div class="doors">
    <p class="doors-label">DOORS OPEN</p>
    <p class="doors-time">7:00PM</p>
  </div>

  <div class="divider" style="top:730px"></div>
  <p class="exclusive">THIS IS A SUPER-EXCLUSIVE EVENT. - ONLY 150 TIX AVAILABLE -</p>
  <div class="divider" style="top:782px"></div>

  <div class="caterer-mark">
    <span class="square"></span>
    <span class="name">Tavolino</span>
  </div>
  <p class="package">
    INCLUDED IN THE TICKET PRICE OF $100 IS 2<br>
    COMPLIMENTARY DRINKS (BEER/WINE/BUBBLY)<br>
    AND LOTS OF DELICIOUS ITALIAN TAPAS<br>
    FOOD FROM 7PM TO 8:30PM - PROVIDED BY<br>
    <span class="highlight">TAVOLINO EVENTS CATERING.</span> EXTRA DRINKS INCLUDING SPIRITS<br>
    AND COCKTAILS CAN BE PURCHASED AT THE BAR.
  </p>
</main>
</body>
</html>
```